Design Large Inspirational Artwork with Long Quote

Design a large piece of art with a quote from Marcus Hallwell.

QUOTE
"The thing that's so interesting about being alive is that you're all in. No matter what you do, you're all in. This is gonna kill you, so I think you might as well play the most magnificent game you can while you're waiting. Because, do you have anything better to do? Why not pick the best thing possible that you could do? Because you're more powerful than you think, way more powerful than you think. I mean, God only knows what you are in the final analysis. You're blind to your own weaknesses, but you're also blind to your own strengths. How far could you take that if you stopped wasting time, and if you stopped lying, and if you oriented yourself to the highest possible good that you could conceive of and you committed to that? How much good could you do? Well, I would say: why don't you find out?"

SIZE
A high-resolution print size of 6' wide and 3' tall should provide ample space for both the quote and the accompanying artwork.

TYPOGRAPHY
Choose a bold, clean, and easily readable font for the quote. You could also experiment with different font sizes for certain words or phrases to emphasize their importance within the quote.

COLORS
Since the quote is thought-provoking and reflective, you might want to use a color palette that evokes a sense of introspection and depth. Consider using cool, calming colors like shades of blue, gray, or green. Alternatively, you can use a contrasting color scheme with a light background and dark text to make the quote stand out.

ARTWORK
Select / create / edit background artwork to complement the quote.
While a great design might be minimalistic and/or greyscale, I'd really like to see some full color options. This might be anything from photography or graphics inspired by the ideas in the text, to abstract colors or illustrations that feel like the sentiment expressed.
The art should capture your attention and encourage you to read the text. The art should be visually appealing, both at a distance and up close, regardless of whether the text is read.
Updates

Having trouble confirming the exact print size.

Still looking for printing solution and final size confirmation.

Target Market(s)

Personal, business, office

Industry/Entity Type

None

Font styles to use
Sans Serif
Script

Requirements
Must have
• Entire quote, legible text, modern design, attractive artwork, approx 6ft wide and 3ft tall
Nice to have
• Different font (sizes) for certain words or phrases to emphasize their importance within the quote.

```html
<!DOCTYPE html>
<html lang="en">
<head>
<meta charset="utf-8">
<title>Why Don't You Find Out – Quote Artwork</title>
<link rel="stylesheet" href="https://fonts.googleapis.com/css2?family=Roboto+Condensed:wght@400;700&display=swap">
<style>
  :root {
    --sky-top: #4fa9cf;
    --sky-mid: #a9d6e0;
    --sun-glow: #f6dc9a;
    --horizon: #d9b878;
    --hills: #6f7a4a;
    --field: #3c5526;
    --field-deep: #1f2e16;
    --rust-light: #a8704a;
    --rust-dark: #6b3d25;
    --ink-blue: #0e6391;
    --ink-blue-strong: #0a5784;
    --ink-light: #ffffff;
  }
  * { margin: 0; padding: 0; box-sizing: border-box; }
  html, body { width: 1200px; height: 600px; overflow: hidden; }
  body { font-family: "Roboto Condensed", "Arial Narrow", sans-serif; }

  .artwork {
    position: relative;
    width: 1200px;
    height: 600px;
    overflow: hidden;
  }

  .landscape-scene {
    position: absolute;
    inset: 0;
    background:
      radial-gradient(ellipse 520px 260px at 160px 340px, rgba(255,236,170,0.95), rgba(255,236,170,0) 70%),
      linear-gradient(180deg,
        var(--sky-top) 0%,
        var(--sky-mid) 28%,
        var(--sun-glow) 50%,
        var(--horizon) 60%,
        var(--hills) 68%,
        var(--field) 82%,
        var(--field-deep) 100%);
  }

  .chain-band {
    position: absolute;
    left: 256px;
    top: 322px;
    width: 944px;
    height: 40px;
    border-radius: 20px 0 0 20px;
    background: linear-gradient(180deg, var(--rust-light), var(--rust-dark));
    opacity: 0.85;
  }

  .quote {
    position: absolute;
    left: 0;
    width: 1262px;
    text-align: center;
    font-size: 32px;
    line-height: 38.8px;
    letter-spacing: -0.2px;
    white-space: nowrap;
  }
  .quote--upper { top: 50px; color: var(--ink-blue); }
  .quote--lower { top: 360px; color: var(--ink-light); }

  .emphasis { font-weight: 700; }
  .quote--upper .emphasis { color: var(--ink-blue-strong); }
</style>
</head>
<body>
  <main class="artwork">
    <div class="landscape-scene" role="img" aria-label="Photograph of a sunlit sky over green hills and meadow, with birds flying free on the left"></div>
    <div class="chain-band" role="img" aria-label="Broken rusty chain stretching across the horizon"></div>

    <p class="quote quote--upper">
      The thing that's so interesting about being alive is that you're all in. Nomatter what<br>
      you do, you're all in. This is gonna kill you, so I think you might as well play the<br>
      most magnificent game&nbsp; you can while you'rewaiting. Because, do you have<br>
      anything better to do ? Why not pick the best thing possible that you could<br>
      do ? <span class="emphasis">Because you're more powerful than you think,</span> way more powerful<br>
      than you think. I mean, God only knows what you are in the final analysis.<br>
      You're blind to your own weaknesses, but you're also blind to your
    </p>

    <p class="quote quote--lower">
      own strengths. How far could you take that if<br>
      you stopped wasting time, and if you stopped lying, and if you oriented yourself<br>
      to the highest possible good that you could conceive of and<br>
      you committed to that ? How much good could you do?<br>
      Well, I would say: <span class="emphasis">why don't you find out?</span>
    </p>
  </main>
</body>
</html>
```